Brightfield Optics seeks updated contemporary business card

Brightfield Optics utilizes advanced technology and we take pride in the modern look and feel of our practice. We like our current card, but it's been four years so it is time for an update.

Target Market(s)

Females 25-45 make the most health care decisions for their family.

Contact Information for Business Card

Clean front. Back with info and with empty space for appointment time or other small note

Requirements
Must have
• Logo
Ridge Marketvale, 28413 E Larkspur Ave
Cedar Terrace Marketvale, 4638 S Dunmore Rd
Call or text: 509-342-1968
email: hello@brightfieldoptics.example
brightfieldoptics.example
Dr Tobias Werring & Associates

```html
<!DOCTYPE html>
<html lang="en">
<head>
<meta charset="utf-8">
<title>Brightfield Optics – Business Card</title>
<link href="https://fonts.googleapis.com/css2?family=Quicksand:wght@500;600;700&display=swap" rel="stylesheet">
<style>
  :root{
    --stage:#272c36;
    --navy:#142a66;
    --navy-deep:#0f1f4f;
    --blue:#1f5fae;
    --sky:#1ea3dc;
    --sky-light:#3bb8ea;
    --paper:#ffffff;
    --rule:#4a4f5a;
    --shadow:rgba(0,0,0,.45);
  }
  *{box-sizing:border-box;margin:0;padding:0}
  html,body{width:1200px;height:876px;overflow:hidden}
  body{background:var(--stage);font-family:"Quicksand",sans-serif;position:relative}

  .card{position:absolute;top:290px;width:520px;height:297px;border-radius:4px;overflow:hidden;box-shadow:0 18px 40px var(--shadow)}
  .card--back{left:50px;background:var(--paper)}
  .card--front{left:630px;background:radial-gradient(ellipse at 70% 35%,#1d3a86 0%,var(--navy) 55%,var(--navy-deep) 100%)}

  /* back side */
  .back__band{position:absolute;left:0;top:0;width:100%;height:160px;background:linear-gradient(100deg,var(--navy) 0%,var(--blue) 45%,var(--sky) 100%)}
  .brand{position:absolute;display:flex;flex-direction:column}
  .brand__row{display:flex;align-items:center;gap:8px}
  .brand__dot{width:12px;height:12px;border-radius:50%;background:var(--sky-light);flex:none}
  .brand__name{font-weight:700;color:var(--paper);letter-spacing:.5px;text-transform:uppercase;line-height:1;white-space:nowrap}
  .brand__tag{font-weight:700;color:var(--paper);text-transform:uppercase;letter-spacing:.4px;margin-top:4px;white-space:nowrap}
  .card--back .brand{left:26px;top:26px}
  .card--back .brand__name{font-size:19px}
  .card--back .brand__tag{font-size:10px;padding-left:20px}

  .practitioner{position:absolute;left:290px;top:56px;color:var(--paper)}
  .practitioner__name{font-weight:700;font-size:17px;line-height:1.1;text-transform:uppercase;white-space:nowrap}
  .practitioner__assoc{font-weight:500;font-size:17px;line-height:1.1;text-transform:uppercase;letter-spacing:.5px}
  .contact{list-style:none;margin-top:8px}
  .contact li{display:flex;align-items:center;gap:6px;font-size:10.5px;font-weight:600;line-height:1.55;white-space:nowrap}
  .contact svg{width:10px;height:10px;flex:none}

  .note{position:absolute;left:26px;top:176px;width:300px}
  .note__row{display:flex;align-items:center;gap:8px;margin-bottom:10px}
  .note__row svg{width:12px;height:12px}
  .note__slash{width:1px;height:12px;background:var(--rule)}
  .note__line{height:1px;background:var(--rule);margin-top:14px;width:290px}
  .locations{position:absolute;left:26px;bottom:16px;color:var(--blue);font-size:11px;font-weight:600;line-height:1.5;list-style:none}

  /* front side */
  .card--front .brand{left:34px;top:40px}
  .card--front .brand__name{font-size:26px}
  .card--front .brand__tag{font-size:12px;padding-left:20px}
  .front__web{position:absolute;left:34px;top:128px;color:var(--sky);font-size:13px;font-weight:500}
  .front__sweep{position:absolute;left:0;bottom:0;width:100%;height:110px;background:linear-gradient(180deg,rgba(30,163,220,0) 0%,rgba(30,163,220,.18) 100%)}
</style>
</head>
<body>

<section class="card card--back" aria-label="Card back">
  <div class="back__band"></div>

  <div class="brand">
    <div class="brand__row"><span class="brand__dot"></span><span class="brand__name">Brightfield Optics</span></div>
    <span class="brand__tag">Advanced Eye Care</span>
  </div>

  <div class="practitioner">
    <p class="practitioner__name">Dr. Tobias Werring &amp;</p>
    <p class="practitioner__assoc">Associates</p>
    <ul class="contact">
      <li><svg viewBox="0 0 12 12" fill="#fff"><path d="M2.5 1l2 .3.6 2.3-1.2.9a7 7 0 0 0 3.6 3.6l.9-1.2 2.3.6.3 2c-.2.8-1 1.5-2 1.5C5 11 1 7 1 3c0-1 .7-1.8 1.5-2z"/></svg>Call or text: 509-342-1968</li>
      <li><svg viewBox="0 0 12 12" fill="#fff"><path d="M1 2.5h10v7H1z"/><path d="M1 2.5l5 4 5-4" stroke="#1f5fae" fill="none" stroke-width="1"/></svg>Email: hello@brightfieldoptics.example</li>
      <li><svg viewBox="0 0 12 12" fill="none" stroke="#fff" stroke-width="1.1"><circle cx="6" cy="6" r="5"/><path d="M1 6h10M6 1c-2 2.5-2 7.5 0 10M6 1c2 2.5 2 7.5 0 10"/></svg>Web: brightfieldoptics.example</li>
    </ul>
  </div>

  <div class="note">
    <div class="note__row">
      <svg viewBox="0 0 12 12" fill="#1f5fae"><rect x="1" y="2" width="10" height="9" rx="1"/><rect x="2" y="5" width="8" height="5" fill="#fff"/><rect x="3" y="0.5" width="1.5" height="3"/><rect x="7.5" y="0.5" width="1.5" height="3"/></svg>
      <span class="note__slash"></span>
    </div>
    <div class="note__row">
      <svg viewBox="0 0 12 12" fill="#1f5fae"><path d="M8.5 1l2.5 2.5-6.5 6.5L1.5 11l1-3z"/></svg>
      <span class="note__slash"></span>
    </div>
    <div class="note__line"></div>
  </div>

  <ul class="locations">
    <li>Ridge Marketvale 28413 E Larkspur Ave</li>
    <li>Cedar Terrace Marketvale 4638 S Dunmore Rd</li>
  </ul>
</section>

<section class="card card--front" aria-label="Card front">
  <div class="brand">
    <div class="brand__row"><span class="brand__dot"></span><span class="brand__name">Brightfield Optics</span></div>
    <span class="brand__tag">Advanced Eye Care</span>
  </div>
  <p class="front__web">brightfieldoptics.example</p>
  <div class="front__sweep" role="img" aria-label="Large decorative brand sweep in light blue and white"></div>
</section>

</body>
</html>
```